Flyer Design Project

Painting and Maintenance
This is what I have as idea as Job description
Refresh, renew & revive your home. from painting to carpentry. Do you guys have any epic unique slogan?
As what we do Residential - Commercial Interior - ExteriorTrim & Molding installationWainscoting - Wallpaper removalCabinet refinishing Woodwork EnamelingDeck & Fence Cleaning & SealingPressure washConcrete & Paver Washing
I would like to have a note that says-Prompt professional service-Free estimates-Insured -"visit us on PalPorch"
I would like new ideas from you guys as well!
Carpentry

```html
<!DOCTYPE html>
<html lang="en">
<head>
<meta charset="utf-8">
<title>Harlowe Painting – Give Your Home a Makeover</title>
<link rel="stylesheet" href="https://fonts.googleapis.com/css2?family=Raleway:wght@300;400;500;600;700&display=swap">
<style>
  :root {
    --brand-red: #cc3b32;
    --paper: #ffffff;
    --ink-light: #ffffff;
    --ink-soft: rgba(255, 255, 255, 0.88);
    --swatch-warm: #b9aca6;
    --swatch-cool: #b7c6d2;
    --stone-grey: #b8b8b6;
  }
  html, body {
    margin: 0;
    padding: 0;
    overflow: hidden;
    background: var(--paper);
  }
  .flyer {
    position: relative;
    width: 789px;
    height: 1200px;
    overflow: hidden;
    background: var(--paper);
    font-family: "Raleway", sans-serif;
    color: var(--ink-light);
  }
  .flyer__shapes {
    position: absolute;
    inset: 0;
    width: 789px;
    height: 1200px;
  }
  .brand {
    position: absolute;
    left: 104px;
    top: 110px;
    display: flex;
    align-items: center;
    gap: 8px;
    color: var(--brand-red);
    font-weight: 700;
  }
  .brand__mark {
    width: 14px;
    height: 14px;
    background: var(--brand-red);
  }
  .brand__name {
    font-size: 17px;
    line-height: 19px;
    letter-spacing: 0.5px;
  }
  .brand__name span { display: block; font-size: 10.5px; }
  .headline {
    position: absolute;
    left: 102px;
    top: 532px;
    margin: 0;
    font-size: 44px;
    line-height: 55px;
    font-weight: 700;
    letter-spacing: 0.2px;
  }
  .intro {
    position: absolute;
    left: 99px;
    top: 699px;
    margin: 0;
    font-size: 19px;
    line-height: 34.5px;
    font-weight: 300;
    white-space: nowrap;
  }
  .tagline {
    position: absolute;
    left: 91px;
    top: 957px;
    margin: 0;
    font-size: 44px;
    line-height: 52px;
    font-weight: 400;
    white-space: nowrap;
  }
  .specialty {
    position: absolute;
    left: 92px;
    top: 1009px;
    margin: 0;
    font-size: 28.5px;
    line-height: 34px;
    font-weight: 500;
    white-space: nowrap;
  }
  .contact {
    position: absolute;
    left: 92px;
    top: 1043px;
    margin: 0;
    font-size: 19.5px;
    line-height: 24px;
    font-weight: 600;
  }
  .services {
    position: absolute;
    left: 92px;
    top: 1082px;
    width: 610px;
    margin: 0;
    font-size: 13.5px;
    line-height: 19px;
    font-weight: 400;
    color: var(--ink-soft);
  }
  .notes {
    position: absolute;
    left: 92px;
    top: 1152px;
    margin: 0;
    padding: 0;
    list-style: none;
    display: flex;
    gap: 18px;
    font-size: 15px;
    line-height: 20px;
    font-weight: 600;
    white-space: nowrap;
  }
  .notes li::before {
    content: "";
    display: inline-block;
    width: 7px;
    height: 7px;
    margin-right: 7px;
    vertical-align: middle;
    background: var(--ink-light);
  }
</style>
</head>
<body>
<main class="flyer">
  <svg class="flyer__shapes" viewBox="0 0 800 1217">
    <path class="panel-red" fill="var(--brand-red)"
          d="M0,575 L255,395 Q290,370 325,395 L800,860 L800,1217 L0,1217 Z"/>
    <rect class="accent-diamond" fill="var(--brand-red)" x="-53" y="-53" width="106" height="106" rx="18"
          transform="translate(133 333) rotate(45)"/>
    <defs>
      <linearGradient id="swatchesLarge" x1="0" y1="0" x2="1" y2="1">
        <stop offset="0" stop-color="#eef0ef"/>
        <stop offset="1" stop-color="#cfd2d0"/>
      </linearGradient>
      <linearGradient id="swatchesWarm" x1="0" y1="0" x2="1" y2="1">
        <stop offset="0" stop-color="#d9c39a"/>
        <stop offset="0.5" stop-color="#c4bcc0"/>
        <stop offset="1" stop-color="var(--swatch-warm)"/>
      </linearGradient>
      <linearGradient id="swatchesCool" x1="0" y1="0" x2="1" y2="1">
        <stop offset="0" stop-color="#d4d6d9"/>
        <stop offset="1" stop-color="var(--swatch-cool)"/>
      </linearGradient>
    </defs>
    <rect class="photo photo--samples" role="img" aria-label="Photo of paint colour cards and countertop samples on a floor plan"
          fill="url(#swatchesLarge)" x="-163" y="-163" width="326" height="326" rx="34"
          transform="translate(655 175) rotate(45)"/>
    <rect class="photo photo--warm-cards" role="img" aria-label="Photo of fanned warm-toned paint colour cards"
          fill="url(#swatchesWarm)" x="-82" y="-82" width="164" height="164" rx="22"
          transform="translate(388 298) rotate(45)"/>
    <rect class="photo photo--cool-cards" role="img" aria-label="Photo of pale blue and grey paint colour cards"
          fill="url(#swatchesCool)" x="-82" y="-82" width="164" height="164" rx="22"
          transform="translate(535 445) rotate(45)"/>
    <rect class="photo photo--stone" role="img" aria-label="Close-up of a grey quartz sample"
          fill="var(--stone-grey)" x="-32" y="-32" width="64" height="64" rx="10"
          transform="translate(742 438) rotate(45)"/>
    <g class="icon-tools" fill="var(--ink-light)">
      <g transform="rotate(-35 450 900)">
        <rect x="444" y="876" width="12" height="78" rx="3"/>
        <rect x="422" y="860" width="52" height="18" rx="3"/>
      </g>
      <g transform="rotate(30 475 895)">
        <rect x="452" y="842" width="46" height="40" rx="4"/>
        <rect x="461" y="882" width="28" height="11"/>
        <rect x="469" y="893" width="12" height="58" rx="4"/>
      </g>
    </g>
  </svg>

  <div class="brand">
    <div class="brand__mark"></div>
    <div class="brand__name">HARLOWE PAINTING<span>&amp; MAINTENANCE LLC.</span></div>
  </div>

  <h1 class="headline">GIVE YOUR<br>HOME A<br>MAKEOVER</h1>
  <p class="intro">Are you looking to refresh, renew and<br>revive your space?<br>Harlowe Painting is the perfect solution<br>for you! We offer end to end support for<br>your Home and Commercial<br>Renovation needs.</p>

  <p class="tagline">• Refresh • Renew • Revive</p>
  <p class="specialty">Home and Commercial Renovation Specialist</p>
  <p class="contact">(Website &amp; Contact Address)</p>

  <p class="services">Residential · Commercial · Interior · Exterior · Carpentry · Trim &amp; Molding Installation · Wainscoting · Wallpaper Removal · Cabinet Refinishing · Woodwork Enameling · Deck &amp; Fence Cleaning &amp; Sealing · Pressure Wash · Concrete &amp; Paver Washing</p>
  <ul class="notes">
    <li>Prompt professional service</li>
    <li>Free estimates</li>
    <li>Insured</li>
    <li>Visit us on PalPorch</li>
  </ul>
</main>
</body>
</html>
```